Wine Label for a White and a Red Wine from Italy

We have a very good idea of what we want with artwork. We need you to please design a 'template' with the text so we can change out the artwork from year to year. Samples are shown of what we are looking for. We are looking for options with the two basic designs. Brand name of wine is: Valora del Torrino. Both wines are in a light green Bordeaux-style bottle (note: we don't show a light green bottle in the mockup but please remember the bottle is light green). Artwork is provided. We'd like to see either the green or blue butterfly on the white wine, the red butterfly is for the red wine. Please base the design on the attached label from Ashby and/or the attached label from Chateau Vellanges.

Target Market(s)

Millennials, women

Requirements
Must have
• The artwork (butterflies) attached.
Nice to have
• Elegant, readable fonts. Please make the text so it can be changed by the printer. Please make it so the artwork can be changed too.

```html
<!DOCTYPE html>
<html lang="en">
<head>
<meta charset="utf-8">
<title>Valora del Torrino – Barrel Select Labels</title>
<link rel="stylesheet" href="https://fonts.googleapis.com/css2?family=Cormorant+Garamond:ital,wght@0,400;0,500;1,400&family=EB+Garamond:ital,wght@0,400;1,400&family=Questrial&display=swap">
<style>
  :root {
    --page: #ffffff;
    --label-paper: #ffffff;
    --ink: #141414;
    --rule-bianco: #d9d3c4;
    --rule-rosso: #8a3a12;
    --shadow: rgba(0, 0, 0, 0.45);
    --cream: #f3efe6;
    --leaf: #8fb63a;
    --leaf-deep: #1f3d1c;
    --saffron: #f4a81c;
    --amber: #e88a12;
    --rust: #a8301a;
  }
  * { margin: 0; padding: 0; box-sizing: border-box; }
  html, body { width: 1200px; height: 849px; overflow: hidden; background: var(--page); }
  .canvas { position: relative; width: 1200px; height: 849px; }

  .label {
    position: absolute;
    width: 372px;
    height: 575px;
    background: var(--label-paper);
    box-shadow: 12px 12px 10px var(--shadow);
    overflow: hidden;
    color: var(--ink);
    text-align: center;
  }
  .label--bianco { left: 170px; top: 125px; background: linear-gradient(160deg, #fbfaf7 0%, #ffffff 55%, #f8f6f1 100%); }
  .label--rosso { left: 650px; top: 131px; }

  .artwork { position: absolute; }
  .label--bianco .artwork {
    left: 60px; top: 150px; width: 270px; height: 250px;
    background:
      radial-gradient(ellipse 40% 38% at 46% 52%, var(--leaf-deep) 0%, rgba(31,61,28,0.7) 45%, rgba(31,61,28,0) 100%),
      radial-gradient(ellipse 55% 45% at 55% 40%, var(--leaf) 0%, rgba(143,182,58,0.5) 50%, rgba(143,182,58,0) 100%),
      radial-gradient(ellipse 60% 60% at 50% 50%, var(--cream) 0%, rgba(243,239,230,0) 100%);
  }
  .label--rosso .artwork {
    left: 18px; top: 35px; width: 340px; height: 460px;
    border-radius: 38% 12% 30% 20% / 18% 20% 30% 40%;
    background:
      radial-gradient(ellipse 32% 18% at 38% 52%, var(--rust) 0%, rgba(168,48,26,0.85) 55%, rgba(168,48,26,0) 100%),
      radial-gradient(ellipse 60% 55% at 55% 45%, var(--saffron) 0%, var(--amber) 60%, rgba(232,138,18,0) 100%);
  }

  .content { position: relative; z-index: 1; }
  .brand {
    font-family: "Cormorant Garamond", serif;
    font-weight: 500;
    font-size: 46px;
    line-height: 1;
    letter-spacing: 1px;
    margin-top: 40px;
  }
  .brand-sub {
    font-family: "EB Garamond", serif;
    font-size: 24px;
    line-height: 1;
    margin-top: 4px;
  }
  .rule { height: 1px; margin: 9px auto 0; }
  .rule--brand { width: 148px; }
  .rule--variety { width: 110px; margin-top: 3px; }
  .label--bianco .rule { background: var(--rule-bianco); }
  .label--rosso .rule { background: var(--rule-rosso); }
  .range {
    font-family: "Questrial", sans-serif;
    font-size: 13.5px;
    letter-spacing: 3.4px;
    margin-top: 9px;
  }
  .variety {
    position: absolute; left: 0; right: 0; top: 436px;
    font-family: "EB Garamond", serif;
    font-size: 16px; letter-spacing: 1px; line-height: 1;
  }
  .vintage {
    font-family: "EB Garamond", serif;
    font-size: 16px; letter-spacing: 1px;
    margin-top: 6px;
  }
  .maker {
    position: absolute; left: 0; right: 0; top: 518px;
    font-family: "Questrial", sans-serif;
    font-size: 7.5px; letter-spacing: 0.2px;
  }
  .origin {
    position: absolute; left: 0; right: 0; top: 533px;
    font-family: "EB Garamond", serif;
    font-style: italic; font-size: 10.5px; letter-spacing: 0.4px;
  }
</style>
</head>
<body>
<main class="canvas">

  <section class="label label--bianco">
    <div class="artwork" role="img" aria-label="Painted green butterfly artwork on soft cream brushstrokes"></div>
    <div class="content">
      <h1 class="brand">VALORA</h1>
      <p class="brand-sub">del Torrino</p>
      <div class="rule rule--brand"></div>
      <p class="range">BARREL SELECT</p>
    </div>
    <div class="variety content">
      <p>BIANCO</p>
      <div class="rule rule--variety"></div>
      <p class="vintage">2018</p>
    </div>
    <p class="maker">ARTISANALLY CRAFTED BY CANTINA TRE COLLINE - SUSTAINABLY FRAMED</p>
    <p class="origin">Piemonte - Italy</p>
  </section>

  <section class="label label--rosso">
    <div class="artwork" role="img" aria-label="Painted red butterfly artwork over bold saffron brushstrokes"></div>
    <div class="content">
      <h1 class="brand">VALORA</h1>
      <p class="brand-sub">del Torrino</p>
      <div class="rule rule--brand"></div>
      <p class="range">BARREL SELECT</p>
    </div>
    <div class="variety content">
      <p>ROSSO</p>
      <div class="rule rule--variety"></div>
      <p class="vintage">2018</p>
    </div>
    <p class="maker">ARTISANALLY CRAFTED BY CANTINA TRE COLLINE - SUSTAINABLY FRAMED</p>
    <p class="origin">Piemonte - Italy</p>
  </section>

</main>
</body>
</html>
```